Church needs a very simple, quality infographic to communicate their process

I just updated the brief with two images of a design idea that I like which I would like to see worked into my brief.
Considering those new pics, I would remove the words "up, in, out" and put in "god, the church, the world". I would put "connect in every direction" somewhere in the design. I would try to represent how we want to connect each person in each of those directions. Lastly, I would try to show a connection between those three things and a person.
Design Needs:A simple infographic that clearly communicates our discipleship pathway without requiring additional explanation. Discipleship Process:• In order for someone in our church to be completely discipled they must “connect in every direction”. They must connect …o Up to God o In to the Churcho Out to the WorldTone and Manner:• The main objective is that someone new to the church could look at the infographic and understand that our church wants to help them connect up to God, in to the church, and out to the world and that’s what they are supposed to do. • Intuitive and obvious to understand.• Simple and clear.• Same color as our logo and values (if possible). • Our church’s mission is “Connecting Young Families to Christ” so our focus is to reach out to families while not being exclusive to others. • Our church’s core values are: Equipping, Serving, Belonging, Missional Living, Spirit-living• Our target audience is families with school-aged kids. • Our website is www.rdvalleychapel.ca • Our church is an evangelical Christian church about 50 years old, located in Mississauga, Canada, and recently went through a church relaunch where we came up with a new mission, vision, and values, and now our discipleship pathway. • I would like the infographic to have a real quality to it which reflects the amount of effort and care we put into crafting our discipleship pathway and how important it is going forward. Further Requests:• I intend to place this infographic on a wall in the main auditorium (5 feet x 5 feet) and be able to place it on documents, posters, website, etc.• Needs to be quality enough to scale way up and resize. • Will need the graphic completed by May 14th.Please contact Lead Pastor, Darren Whitlock darren@rdvalleychapel.ca

```html
<!DOCTYPE html>
<html lang="en">
<head>
<meta charset="utf-8">
<title>Connect in Every Direction – Ridge Valley Chapel</title>
<link href="https://fonts.googleapis.com/css2?family=Montserrat:wght@600;700;800&display=swap" rel="stylesheet">
<style>
  :root {
    --purple: #8e2a8c;
    --blue: #1c75bc;
    --orange: #f7941d;
    --white: #ffffff;
    --ink: #2b2b2b;
  }
  html, body {
    margin: 0;
    padding: 0;
    width: 1200px;
    height: 1200px;
    overflow: hidden;
    background: var(--white);
  }
  .infographic {
    display: block;
    width: 1200px;
    height: 1200px;
  }
  .banner-title {
    font-family: "Montserrat", sans-serif;
    font-weight: 800;
    font-size: 31px;
    letter-spacing: 2px;
    fill: var(--purple);
  }
  .direction-label {
    font-family: "Montserrat", sans-serif;
    font-weight: 700;
    font-size: 36px;
    fill: var(--white);
  }
  .church-name {
    font-family: "Montserrat", sans-serif;
    font-weight: 700;
    font-size: 21px;
    fill: var(--ink);
  }
  .connector {
    fill: none;
    stroke: var(--white);
    stroke-width: 5;
    stroke-dasharray: 16 13;
    stroke-linecap: round;
  }
  .node-ring {
    fill: none;
    stroke: var(--white);
    stroke-width: 6;
  }
  .node-disc { fill: var(--white); }
  .person-part { fill: var(--white); }
</style>
</head>
<body>
<svg class="infographic" viewBox="0 0 1200 1200" xmlns="http://www.w3.org/2000/svg">
  <!-- background segments -->
  <rect class="segment segment--god" width="1200" height="1200" fill="var(--purple)"/>
  <polygon class="segment segment--world" points="1200,225 630,810 1200,1200" fill="var(--blue)"/>
  <polygon class="segment segment--church" points="0,458 630,810 1200,1200 0,1200" fill="var(--orange)"/>

  <!-- title banner -->
  <path class="banner" d="M150,0 H1050 L1030,50 Q1018,82 985,82 H215 Q182,82 170,50 Z" fill="var(--white)"/>
  <text class="banner-title" x="600" y="52" text-anchor="middle">CONNECT IN EVERY DIRECTION</text>

  <!-- connectors -->
  <path class="connector" d="M638,503 C650,570 560,610 535,660 C515,700 530,760 555,800"/>
  <path class="connector" d="M505,865 C470,845 450,870 440,920 C425,990 380,1010 300,1020"/>
  <path class="connector" d="M730,880 C780,905 810,890 820,820 C830,700 890,640 925,640"/>

  <!-- to God -->
  <text class="direction-label" x="622" y="200" text-anchor="middle">to God</text>
  <circle class="node-ring" cx="622" cy="360" r="143"/>
  <circle class="node-disc" cx="622" cy="360" r="128"/>
  <g class="icon-cross" fill="var(--purple)">
    <rect x="607" y="272" width="30" height="172"/>
    <rect x="557" y="303" width="130" height="30"/>
  </g>

  <!-- to the World -->
  <text class="direction-label" x="1022" y="600" text-anchor="middle">to the World</text>
  <circle class="node-ring" cx="1027" cy="757" r="140"/>
  <circle class="node-disc" cx="1027" cy="757" r="126"/>
  <circle class="globe" role="img" aria-label="Globe showing the continents" cx="1027" cy="757" r="95" fill="var(--blue)"/>

  <!-- to the Church -->
  <text class="direction-label" x="200" y="780" text-anchor="middle">to the Church</text>
  <circle class="node-ring" cx="177" cy="945" r="140"/>
  <circle class="node-disc" cx="177" cy="945" r="126"/>
  <text class="church-name" x="177" y="953" text-anchor="middle">Ridge Valley Chapel</text>

  <!-- person pictogram -->
  <g class="person" role="img" aria-label="A person connected to God, the church and the world">
    <circle class="person-part person-head" cx="618" cy="735" r="48"/>
    <path class="person-part person-shoulders" d="M505,845 V830 Q505,797 540,797 H695 Q730,797 730,830 V845 Z"/>
    <rect class="person-part person-arm" x="505" y="830" width="50" height="225" rx="18"/>
    <rect class="person-part person-arm" x="680" y="830" width="50" height="225" rx="18"/>
    <rect class="person-part person-torso" x="562" y="830" width="113" height="225"/>
    <rect class="person-part person-leg" x="562" y="1050" width="52" height="150"/>
    <rect class="person-part person-leg" x="622" y="1050" width="53" height="150"/>
  </g>
</svg>
</body>
</html>
```